"Recently Leased" flyer for real estate agency

Looking to have a Recently Leased flyer designed. This will be delivered to apartments and houses closely situated to a property we have recently leased. The idea is to get the attention of owner/landlords in the area that may be considering leasing their property in the future and inform them of the great work we are doing locally. I would like the design to be a two sided flyer using the photoshop (PSD) template below (we would like to be able to edit this once complete should we need to update copy etc in the future). I would like the front page to look like our "for lease sign with the leased sticker on it and copy, I dont want it to look like a typical junk mail flyer.

Target Market(s)

Property owners and investors, male and female aged 28-70

Industry/Entity Type

Real Estate

Font styles to use
Sans Serif

Colors

Designer to choose colors to be used in the design.

Requirements
Must have
• Harbor Keystone Logo
• Contact information
• Copy supplied
Nice to have
• Slick, clean design,
Should not have
• too many colours or too busy a design.
• NO PROPERTY PHOTOS ON FRONT - I want this to be generic and not relate to a specific property image which might confuse people.

```html
<!DOCTYPE html>
<html lang="en">
<head>
<meta charset="utf-8">
<title>Harbor Keystone – Leased Flyer</title>
<link href="https://fonts.googleapis.com/css2?family=Lato:wght@400;700;900&display=swap" rel="stylesheet">
<style>
  :root {
    --backdrop: #d1d2d4;
    --paper: #f1f1f1;
    --ink: #2b2b2b;
    --body: #3a3a3a;
    --muted: #555555;
    --red: #b5353a;
    --tick: #c9302f;
    --teal: #2e7b8c;
    --strip: #d0282e;
    --rule: #8a8a8a;
  }
  * { box-sizing: border-box; margin: 0; padding: 0; }
  html, body { width: 1022px; height: 1200px; overflow: hidden; }
  body {
    background: var(--backdrop);
    font-family: "Lato", sans-serif;
    color: var(--body);
    position: relative;
  }
  .flyer {
    position: absolute;
    top: 185px;
    width: 383px;
    height: 830px;
    background: var(--paper);
  }
  .flyer--front { left: 95px; }
  .flyer--back { left: 545px; }

  .brand {
    position: absolute;
    left: 0; right: 0;
    display: flex;
    align-items: center;
    justify-content: center;
    gap: 8px;
    font-weight: 900;
    font-size: 29px;
    letter-spacing: 0.2px;
    color: var(--ink);
  }
  .brand__dot { width: 12px; height: 12px; background: var(--teal); }
  .flyer--front .brand { top: 86px; }
  .flyer--back .brand { top: 630px; }

  .leased-sticker {
    position: absolute;
    left: 33px; top: 201px;
    width: 314px; height: 74px;
    background: var(--red);
    padding: 5px;
  }
  .leased-sticker__frame {
    width: 100%; height: 100%;
    border: 2px solid #fff;
    display: flex; align-items: center; justify-content: center;
    color: #fff;
    font-size: 66px;
    font-weight: 400;
    letter-spacing: 1px;
    line-height: 1;
  }

  .copy {
    position: absolute;
    left: 40px;
    width: 304px;
    font-size: 12px;
    line-height: 15px;
  }
  .copy p + p { margin-top: 5px; }
  .copy--justify { text-align: justify; }

  .ticks { list-style: none; }
  .ticks li {
    position: relative;
    padding-left: 20px;
    margin-bottom: 5px;
    font-size: 11.8px;
    line-height: 15px;
  }
  .ticks svg { position: absolute; left: 0; top: 3px; }

  .flyer--front .intro { top: 298px; }
  .flyer--front .ticks { position: absolute; left: 64px; top: 409px; width: 270px; }
  .flyer--front .closing { top: 646px; }

  .hero-photo {
    position: absolute; left: 0; top: 0;
    width: 383px; height: 183px;
    background: linear-gradient(180deg, #5f9fcb 0%, #a9cbe0 30%, #6f7a72 52%, #4d7a3f 75%, #cfd3cf 100%);
  }
  .flyer--back .intro { top: 201px; }
  .flyer--back .ticks { position: absolute; left: 64px; top: 258px; width: 270px; }
  .flyer--back .closing { top: 509px; }

  .contact {
    position: absolute;
    left: 40px; top: 718px;
    width: 310px;
    display: flex;
    align-items: flex-start;
  }
  .contact__person { width: 140px; color: var(--muted); }
  .contact__name { font-size: 17px; line-height: 20px; font-weight: 400; }
  .contact__phone { font-size: 17px; font-weight: 700; display: flex; align-items: center; gap: 2px; line-height: 20px; }
  .contact__divider {
    width: 1px; height: 50px; background: var(--rule);
    margin-top: -5px; position: relative;
  }
  .contact__pin { position: absolute; left: -7px; top: 15px; }
  .contact__office { padding-left: 20px; color: var(--muted); }
  .contact__office strong { display: block; font-size: 13.5px; font-weight: 700; line-height: 16px; margin-top: -3px; }
  .contact__office span { display: block; font-size: 10.5px; line-height: 13px; margin-top: 2px; }

  .footer-band {
    position: absolute; left: 0; bottom: 0;
    width: 100%; height: 54px;
    background: var(--teal);
    color: #fff;
    text-align: center;
    font-size: 13px;
    line-height: 18px;
    letter-spacing: 0.3px;
    padding-top: 9px;
    padding-right: 11px;
  }
  .footer-band::after {
    content: ""; position: absolute; right: 0; top: 0;
    width: 11px; height: 100%; background: var(--strip);
  }
</style>
</head>
<body>
<svg width="0" height="0" style="position:absolute">
  <defs>
    <symbol id="tick" viewBox="0 0 10 10">
      <circle cx="5" cy="5" r="5" fill="#c9302f"/>
      <path d="M2.7 5.1 L4.4 6.7 L7.4 3.5" fill="none" stroke="#fff" stroke-width="1.4" stroke-linecap="round" stroke-linejoin="round"/>
    </symbol>
    <symbol id="pin" viewBox="0 0 14 14">
      <circle cx="7" cy="7" r="7" fill="#555"/>
      <path d="M7 3.2a2.6 2.6 0 0 0-2.6 2.6C4.4 7.8 7 10.8 7 10.8s2.6-3 2.6-5A2.6 2.6 0 0 0 7 3.2z" fill="#fff"/>
      <circle cx="7" cy="5.8" r="1" fill="#555"/>
    </symbol>
    <symbol id="phone" viewBox="0 0 14 14">
      <path d="M3 1.5l2 2.6-1.1 1.4c.8 1.7 2 2.9 3.6 3.7l1.4-1.1 2.6 2-1.2 2.1C6 11.7 2.3 8 1 3.1z" fill="none" stroke="#555" stroke-width="1.3" stroke-linejoin="round"/>
    </symbol>
  </defs>
</svg>

<section class="flyer flyer--front">
  <div class="brand"><span>HARBOR KEYSTONE</span><span class="brand__dot"></span></div>

  <div class="leased-sticker"><div class="leased-sticker__frame">LEASED!</div></div>

  <div class="copy copy--justify intro">
    <p>We recently leased a property in your building or street. Attracting a great reliable tenant and fantastic return for the owner.</p>
    <p>We received a high number of enquires and applications for this property and have a database of screened and qualified tenants looking to lease in your area.</p>
  </div>

  <ul class="ticks">
    <li><svg width="10" height="10"><use href="#tick"/></svg>On average we lease properties 2 weeks faster than the Northern Beaches average</li>
    <li><svg width="10" height="10"><use href="#tick"/></svg>Strong database of tenants actively looking in the area</li>
    <li><svg width="10" height="10"><use href="#tick"/></svg>All we do is lease property, no sales – so tenanting and managing your property is our priority</li>
    <li><svg width="10" height="10"><use href="#tick"/></svg>90 day money back guarantee on our level of service</li>
    <li><svg width="10" height="10"><use href="#tick"/></svg>Highly competitive, simple all-inclusive pricing.</li>
    <li><svg width="10" height="10"><use href="#tick"/></svg>Experience the difference of a property management specialist</li>
  </ul>

  <div class="copy closing">
    <p>Contact <strong>Sam</strong> to get your free rental appraisal or transfer your existing investment to an agency that will give it the attention it deserves and maxamise your return.</p>
  </div>

  <div class="contact">
    <div class="contact__person">
      <div class="contact__name">Sam Carter</div>
      <div class="contact__phone"><svg width="13" height="13"><use href="#phone"/></svg>0400 555 218</div>
    </div>
    <div class="contact__divider"><svg class="contact__pin" width="14" height="14"><use href="#pin"/></svg></div>
    <div class="contact__office">
      <strong>Harbor Keystone Agency</strong>
      <span>Level 1, 18 Coral Tree Rd,</span>
      <span style="margin-top:0">Seacliff NSW 2104</span>
    </div>
  </div>

  <div class="footer-band">sam@harborkeystoneagency.com.au<br>www.harborkeystoneagency.com.au</div>
</section>

<section class="flyer flyer--back">
  <div class="hero-photo" role="img" aria-label="Photo of a row of modern terraced homes with landscaped gardens and steps beside a street under a blue sky"></div>

  <div class="copy copy--justify intro">
    <p>The fundamental idea behind Harbor Keystone Agency was to give landlords a simple and confidence inspiring experience. We achieve this through:</p>
  </div>

  <ul class="ticks">
    <li><svg width="10" height="10"><use href="#tick"/></svg>Unique marketing that goes beyond the standard listing sites and has seen our average days-on-market at 5.9days for 2018.</li>
    <li><svg width="10" height="10"><use href="#tick"/></svg>A simple, yet competitive fee structure.</li>
    <li><svg width="10" height="10"><use href="#tick"/></svg>Excellent customer service through an experienced professional property manager.</li>
    <li><svg width="10" height="10"><use href="#tick"/></svg>Sound advice and communication through out the leasing and management process.</li>
    <li><svg width="10" height="10"><use href="#tick"/></svg>A simple yet powerful landlord portal which enables owners to view media rich inspection reports, financial reports and maintenance progress at anytime.</li>
    <li><svg width="10" height="10"><use href="#tick"/></svg>We then back our service promise with a 90day money back guarantee.</li>
  </ul>

  <div class="copy copy--justify closing">
    <p>If you have been considering leasing your property, purchasing a local investment or aren't happy with your current managing agency, please don't hesitate to contact your local rental specialist for more information:</p>
  </div>

  <div class="brand"><span>HARBOR KEYSTONE</span><span class="brand__dot"></span></div>

  <div class="contact">
    <div class="contact__person">
      <div class="contact__name">Sam Carter</div>
      <div class="contact__phone"><svg width="13" height="13"><use href="#phone"/></svg>0400 555 218</div>
    </div>
    <div class="contact__divider"><svg class="contact__pin" width="14" height="14"><use href="#pin"/></svg></div>
    <div class="contact__office">
      <strong>Harbor Keystone Agency</strong>
      <span>Level 1, 18 Coral Tree Rd,</span>
      <span style="margin-top:0">Seacliff NSW 2104</span>
    </div>
  </div>

  <div class="footer-band">sam@harborkeystoneagency.com.au<br>www.harborkeystoneagency.com.au</div>
</section>
</body>
</html>
```